Crafted Ember Website

Would like a website designed for my fitness and nutrition coaching company Craft Ember. I have a company logo and would like to keep the page layout clean and simple. Needs to look great on computer and mobile devices.

Target Market(s)

Target market is individuals looking to make changes in their health and nutrition with the help of an online coach.

Industry/Entity Type

Fitness

Number of Pages Required

2 page

Colors
3176b5
0355a3
85acd3
cedeed
f8fcfd
ffffff

Requirements
Must have
• The first page should have the company logo and name towards the top and below that client before and after photos scrolling or displaying in some manner. Also would like a section that states services offered and a section about myself since I am the primary coach for clients.

```html
<!DOCTYPE html>
<html lang="en">
<head>
<meta charset="utf-8">
<title>Crafted Ember — Fitness &amp; Nutrition Coaching</title>
<link rel="stylesheet" href="https://fonts.googleapis.com/css2?family=Raleway:wght@400;500;600;700;800&family=Open+Sans:wght@400;600;700&display=swap">
<style>
:root{
  --blue:#3176b5;
  --navy:#0355a3;
  --sky:#85acd3;
  --mist:#cedeed;
  --snow:#f8fcfd;
  --white:#ffffff;
  --ink:#2f3439;
  --grey:#6d747b;
  --line:#e3e8ee;
  --accent:#e8452c;
  --footer:#2c2e33;
}
*{box-sizing:border-box;margin:0;padding:0}
html,body{width:1200px;height:2504px;overflow:hidden}
body{font-family:"Open Sans",Arial,sans-serif;color:var(--ink);background:var(--white);position:relative}

/* top bar */
.topbar{height:30px;display:flex;justify-content:space-between;align-items:center;padding:0 150px;font-size:12px;color:var(--blue);border-bottom:1px solid var(--line)}
.topbar span{display:flex;align-items:center;gap:6px}

/* nav */
.nav{height:58px;display:flex;justify-content:space-between;align-items:center;padding:0 150px;border-bottom:1px solid var(--line)}
.brand{display:flex;align-items:center;gap:8px;font-family:"Raleway",sans-serif;font-weight:700;font-size:15px;color:var(--blue);letter-spacing:1px}
.brand-mark{width:30px;height:30px;background:var(--blue);border-radius:50%}
.menu{display:flex;height:100%}
.menu a{display:flex;align-items:center;padding:0 22px;font-family:"Raleway",sans-serif;font-size:11px;font-weight:600;color:var(--ink);text-decoration:none;border-left:1px solid var(--line);letter-spacing:.5px}
.menu a:last-child{border-right:1px solid var(--line)}
.menu a.active{color:var(--blue);box-shadow:inset 0 -3px 0 var(--blue)}

/* hero */
.hero{position:relative;height:332px;background:linear-gradient(180deg,#e6e9ec,#c9ced3);overflow:hidden}
.hero-photo{position:absolute;top:14px;width:230px;height:318px;background:linear-gradient(180deg,#c89a7e,#8d6350 70%,#3a3d44)}
.hero-photo.before{left:250px}
.hero-photo.after{left:720px}
.hero-title{position:absolute;top:160px;left:0;right:0;text-align:center;font-family:"Raleway",sans-serif;font-weight:500;font-size:46px;color:var(--white);letter-spacing:1px;text-shadow:0 2px 6px rgba(0,0,0,.35)}
.hero-actions{position:absolute;top:232px;left:0;right:0;display:flex;justify-content:center;gap:14px}
.btn{font-family:"Raleway",sans-serif;font-size:11px;font-weight:700;color:var(--white);padding:10px 26px;letter-spacing:.5px}
.btn.primary{background:var(--accent)}
.btn.dark{background:#4a4f56}
.hero-arrow{position:absolute;top:150px;width:26px;height:26px}
.hero-arrow.left{left:20px}.hero-arrow.right{right:20px}

/* welcome */
.welcome{height:580px;padding-top:160px;text-align:center;background:var(--white)}
.section-title{font-family:"Raleway",sans-serif;font-weight:500;color:var(--blue);font-size:34px;line-height:1.15;letter-spacing:1px}
.section-title small{display:block;font-size:24px;letter-spacing:3px}
.divider{width:60px;height:2px;background:var(--blue);margin:14px auto 0}
.intro{width:720px;margin:20px auto 0;font-size:12px;line-height:1.7;color:var(--grey)}
.services{display:flex;justify-content:center;gap:28px;margin-top:44px}
.service{width:270px;height:130px;border:1px solid var(--line);background:var(--snow);position:relative;text-align:left;padding:38px 20px 0}
.service-icon{position:absolute;top:-22px;left:112px;width:46px;height:46px;border-radius:50%;background:var(--white);border:1px solid var(--mist);display:flex;align-items:center;justify-content:center}
.service h3{font-family:"Raleway",sans-serif;font-size:13px;font-weight:700;color:var(--blue);letter-spacing:.5px}
.service h4{font-size:10px;font-weight:600;color:var(--sky);margin:2px 0 6px}
.service p{font-size:10px;line-height:1.55;color:var(--grey)}

/* why choose */
.why{position:relative;height:500px;display:flex}
.why-graphic{width:480px;height:500px;background:radial-gradient(circle at 60% 50%,var(--snow) 0,var(--mist) 45%,var(--sky) 70%,var(--blue) 100%)}
.why-photo{flex:1;background:linear-gradient(120deg,#cfd6dc,#9aa5ae 55%,#5f9bc4)}
.why-panel{position:absolute;left:492px;top:118px;width:300px;height:300px;background:rgba(255,255,255,.95);padding:24px 26px;border-left:4px solid var(--blue)}
.why-panel h2{font-family:"Raleway",sans-serif;font-size:28px;font-weight:600;color:var(--blue);letter-spacing:.5px}
.why-panel p{margin-top:16px;font-size:12px;line-height:1.75;color:var(--grey)}

/* stats */
.stats{height:120px;background:var(--navy);display:flex;justify-content:center;gap:170px;align-items:center;color:var(--white)}
.stat{display:flex;align-items:center;gap:12px}
.stat strong{display:block;font-family:"Raleway",sans-serif;font-size:28px;font-weight:600;line-height:1}
.stat span{font-size:11px;color:var(--mist)}

/* workout */
.workout{height:420px;padding-top:44px;text-align:center;background:var(--white)}
.workout .section-title{font-size:24px;color:var(--ink);font-weight:700;letter-spacing:0}
.workout .divider{background:var(--navy)}
.cards{display:flex;justify-content:center;gap:32px;margin-top:34px}
.card{width:280px;height:268px;border:1px solid var(--line);text-align:left;background:var(--white);box-shadow:0 2px 6px rgba(0,0,0,.06)}
.card-photo{height:128px}
.card-photo.a{background:linear-gradient(135deg,#dbe4ea,#7fb8d8)}
.card-photo.b{background:linear-gradient(135deg,#e4e8eb,#9fb2c2)}
.card-photo.c{background:linear-gradient(135deg,#d7dde2,#b9876d)}
.card-body{padding:12px 16px}
.card-body h3{font-family:"Raleway",sans-serif;font-size:12px;font-weight:700;color:var(--blue)}
.card-body p{margin-top:8px;font-size:10px;line-height:1.6;color:var(--grey)}
.card-body a{display:inline-block;margin-top:10px;font-size:10px;font-weight:700;color:var(--blue);text-decoration:none}

/* contact */
.contact{position:relative;height:360px;background:linear-gradient(180deg,#eef1f3,#dfe4e8)}
.map{position:absolute;inset:0;background:linear-gradient(135deg,#f1f3f5,#dde2e6)}
.contact-boxes{position:absolute;top:112px;left:0;right:0;display:flex;justify-content:center;gap:132px}
.contact-box{position:relative;width:208px;height:168px;background:var(--navy);padding:8px}
.contact-box .inner{height:100%;border:1px solid rgba(255,255,255,.55);display:flex;flex-direction:column;align-items:center;justify-content:center;text-align:center;color:var(--white);padding:0 14px}
.contact-box h3{font-family:"Raleway",sans-serif;font-size:13px;font-weight:700;letter-spacing:.5px}
.contact-box p{margin-top:10px;font-size:11px;line-height:1.5}
.contact-tab{position:absolute;top:-26px;left:76px;width:56px;height:40px;background:var(--navy);display:flex;align-items:center;justify-content:center}

/* footer */
.footer{height:104px;background:var(--footer);display:flex;align-items:center;justify-content:space-between;padding:0 150px;color:#aeb3b9;font-size:11px}
.social{display:flex;gap:14px}
.social span{width:16px;height:16px;border-radius:50%;background:#8b9097}
.footer .brand{color:var(--white);flex-direction:column;gap:6px;font-size:13px}
</style>
</head>
<body>

<header>
  <div class="topbar">
    <span><svg width="12" height="12" viewBox="0 0 24 24"><path fill="#3176b5" d="M6.6 10.8a15 15 0 0 0 6.6 6.6l2.2-2.2a1 1 0 0 1 1-.3 11 11 0 0 0 3.6.6 1 1 0 0 1 1 1V20a1 1 0 0 1-1 1A17 17 0 0 1 3 4a1 1 0 0 1 1-1h3.5a1 1 0 0 1 1 1 11 11 0 0 0 .6 3.6 1 1 0 0 1-.3 1z"/></svg>(555) 014-2287</span>
    <span><svg width="13" height="10" viewBox="0 0 26 20"><rect x="1" y="1" width="24" height="18" fill="none" stroke="#3176b5" stroke-width="2"/><path d="M1 1l12 10L25 1" fill="none" stroke="#3176b5" stroke-width="2"/></svg>hello@craftedember.com</span>
  </div>
  <nav class="nav">
    <div class="brand"><span class="brand-mark"></span>CRAFTED EMBER</div>
    <div class="menu">
      <a class="active" href="#">HOME</a><a href="#">ABOUT US</a><a href="#">FITNESS</a><a href="#">COACHING</a><a href="#">BLOG</a><a href="#">CONTACT</a>
    </div>
  </nav>
</header>

<section class="hero">
  <div class="hero-photo before" role="img" aria-label="Client before photo, shirtless man standing"></div>
  <div class="hero-photo after" role="img" aria-label="Client after photo, same man with toned physique"></div>
  <h1 class="hero-title">AFTER AND BEFORE CRAFTED EMBER</h1>
  <div class="hero-actions"><span class="btn primary">EXPLORE</span><span class="btn dark">READ MORE</span></div>
  <svg class="hero-arrow left" viewBox="0 0 26 26"><path d="M16 5l-8 8 8 8" fill="none" stroke="#fff" stroke-width="2.5"/></svg>
  <svg class="hero-arrow right" viewBox="0 0 26 26"><path d="M10 5l8 8-8 8" fill="none" stroke="#fff" stroke-width="2.5"/></svg>
</section>

<section class="welcome">
  <h2 class="section-title">WELCOME TO<small>CRAFTED EMBER</small></h2>
  <div class="divider"></div>
  <p class="intro">We help busy people build strength, eat well and keep the change for good. Every plan is written for you, checked each week and adjusted as your body and schedule shift. Real coaching, real results, no guesswork.</p>
  <div class="services">
    <article class="service">
      <div class="service-icon"><svg width="22" height="22" viewBox="0 0 24 24"><circle cx="9" cy="8" r="3.5" fill="none" stroke="#3176b5" stroke-width="2"/><path d="M2 20c0-4 3-6 7-6s7 2 7 6" fill="none" stroke="#3176b5" stroke-width="2"/><circle cx="17" cy="9" r="2.5" fill="none" stroke="#3176b5" stroke-width="1.6"/></svg></div>
      <h3>COACHING</h3><h4>One coach, one plan</h4>
      <p>Weekly check-ins keep you on track and moving forward with a clear next step.</p>
    </article>
    <article class="service">
      <div class="service-icon"><svg width="22" height="22" viewBox="0 0 24 24"><path d="M12 20s-8-5-8-11a4.5 4.5 0 0 1 8-2.8A4.5 4.5 0 0 1 20 9c0 6-8 11-8 11z" fill="none" stroke="#3176b5" stroke-width="2"/><path d="M5 12h4l1.5-2.5 2 4.5 1.5-2h5" fill="none" stroke="#3176b5" stroke-width="1.6"/></svg></div>
      <h3>FITNESS</h3><h4>Train smarter, not longer</h4>
      <p>Workouts built around your gym, your time and the goals that matter to you.</p>
    </article>
    <article class="service">
      <div class="service-icon"><svg width="22" height="22" viewBox="0 0 24 24"><circle cx="12" cy="12" r="8" fill="none" stroke="#3176b5" stroke-width="2"/><path d="M12 4v8l5 4" fill="none" stroke="#3176b5" stroke-width="2"/></svg></div>
      <h3>NUTRITION</h3><h4>Food that fits your life</h4>
      <p>Simple meal guidance you can follow at home, at work or on the road.</p>
    </article>
  </div>
</section>

<section class="why">
  <div class="why-graphic" role="img" aria-label="Decorative blue ring graphic listing coaching areas: yoga, nutrition, fitness, body building and training"></div>
  <div class="why-photo" role="img" aria-label="Woman with earphones running on a treadmill in a gym"></div>
  <div class="why-panel">
    <h2>WHY CHOOSE US</h2>
    <p>I coach every client myself. You get direct answers, honest feedback and a plan that grows with you from the first week to the last. No templates, no hand-offs, just steady progress you can see.</p>
  </div>
</section>

<section class="stats">
  <div class="stat"><svg width="30" height="30" viewBox="0 0 24 24"><circle cx="12" cy="8" r="4" fill="none" stroke="#fff" stroke-width="1.6"/><path d="M4 21c0-4.5 3.5-7 8-7s8 2.5 8 7" fill="none" stroke="#fff" stroke-width="1.6"/></svg><div><strong>1000+</strong><span>Happy users</span></div></div>
  <div class="stat"><svg width="30" height="30" viewBox="0 0 24 24"><path d="M3 4h18v12H9l-5 4v-4H3z" fill="none" stroke="#fff" stroke-width="1.6"/></svg><div><strong>5632</strong><span>Comments</span></div></div>
  <div class="stat"><svg width="30" height="30" viewBox="0 0 24 24"><path d="M8 6l-6 6 6 6M16 6l6 6-6 6" fill="none" stroke="#fff" stroke-width="1.6"/></svg><div><strong>25000+</strong><span>Lines of code</span></div></div>
</section>

<section class="workout">
  <h2 class="section-title">WORKOUT OF THE DAY</h2>
  <div class="divider"></div>
  <div class="cards">
    <article class="card">
      <div class="card-photo a" role="img" aria-label="Woman lifting a dumbbell in a bright gym"></div>
      <div class="card-body"><h3>MORNING DUMBBELL CIRCUIT</h3><p>Three rounds, twelve reps each, rest sixty seconds between sets.</p><a href="#">› READ MORE</a></div>
    </article>
    <article class="card">
      <div class="card-photo b" role="img" aria-label="Group cycling class on spin bikes"></div>
      <div class="card-body"><h3>GROUP SPIN INTERVALS</h3><p>Forty minutes of climbs and sprints to lift your heart rate.</p><a href="#">› READ MORE</a></div>
    </article>
    <article class="card">
      <div class="card-photo c" role="img" aria-label="Woman stretching on an exercise mat"></div>
      <div class="card-body"><h3>CORE AND MAT STRETCH</h3><p>A calm session to build core control and loosen tight hips.</p><a href="#">› READ MORE</a></div>
    </article>
  </div>
</section>

<section class="contact">
  <div class="map" role="img" aria-label="Faint street map background"></div>
  <div class="contact-boxes">
    <div class="contact-box">
      <div class="contact-tab"><svg width="20" height="20" viewBox="0 0 24 24"><path fill="#fff" d="M6.6 10.8a15 15 0 0 0 6.6 6.6l2.2-2.2a1 1 0 0 1 1-.3 11 11 0 0 0 3.6.6 1 1 0 0 1 1 1V20a1 1 0 0 1-1 1A17 17 0 0 1 3 4a1 1 0 0 1 1-1h3.5a1 1 0 0 1 1 1 11 11 0 0 0 .6 3.6 1 1 0 0 1-.3 1z"/></svg></div>
      <div class="inner"><h3>PHONE NUMBER</h3><p>(555) 014-2287</p></div>
    </div>
    <div class="contact-box">
      <div class="contact-tab"><svg width="22" height="16" viewBox="0 0 26 20"><rect x="1" y="1" width="24" height="18" fill="none" stroke="#fff" stroke-width="2"/><path d="M1 1l12 10L25 1" fill="none" stroke="#fff" stroke-width="2"/></svg></div>
      <div class="inner"><h3>EMAIL ID</h3><p>hello@craftedember.com</p></div>
    </div>
    <div class="contact-box">
      <div class="contact-tab"><svg width="18" height="22" viewBox="0 0 18 24"><path d="M9 1a7 7 0 0 0-7 7c0 6 7 14 7 14s7-8 7-14a7 7 0 0 0-7-7z" fill="none" stroke="#fff" stroke-width="2"/><circle cx="9" cy="8" r="2.5" fill="#fff"/></svg></div>
      <div class="inner"><h3>ADDRESS</h3><p>48 Harbor Lane, Suite 210, Millbrook, NC 27501</p></div>
    </div>
  </div>
</section>

<footer class="footer">
  <div class="social"><span></span><span></span><span></span><span></span><span></span></div>
  <div class="brand"><span class="brand-mark"></span>CRAFTED EMBER</div>
  <div>© Copyright 2015 CRAFTED EMBER</div>
</footer>

</body>
</html>
```